Boutique Barre Studio in Geneva

Business card for pilates and dance studio. We are a brand new studio and love our fresh image with our yellow color. This business card is meant for our founder.

```html
<!DOCTYPE html>
<html lang="en">
<head>
<meta charset="utf-8">
<title>Arabesque Studio – Business Card</title>
<link href="https://fonts.googleapis.com/css2?family=Montserrat:wght@300;400&family=Oswald:wght@400&display=swap" rel="stylesheet">
<style>
  :root {
    --backdrop: #333333;
    --card-yellow: #f3e888;
    --ink-white: #ffffff;
    --card-shadow: rgba(0, 0, 0, 0.85);
  }
  * { margin: 0; padding: 0; box-sizing: border-box; }
  html, body {
    width: 1027px;
    height: 1200px;
    overflow: hidden;
    background: var(--backdrop);
  }
  .canvas {
    position: relative;
    width: 1027px;
    height: 1200px;
  }
  .card {
    position: absolute;
    left: 216px;
    width: 595px;
    height: 368px;
    background: var(--card-yellow);
    box-shadow: 5px 6px 3px var(--card-shadow);
    color: var(--ink-white);
    overflow: hidden;
  }
  .card--front { top: 174px; }
  .card--back { top: 624px; }

  .wordmark {
    position: absolute;
    font-family: 'Oswald', sans-serif;
    font-weight: 400;
    color: var(--ink-white);
    white-space: nowrap;
    line-height: 1;
  }
  .card--front .wordmark {
    left: 34px;
    top: 72px;
    width: 192px;
    font-size: 28px;
    letter-spacing: 0.5px;
  }
  .card--back .wordmark {
    left: 0;
    right: 0;
    top: 160px;
    text-align: center;
    font-size: 41px;
    letter-spacing: 0.8px;
  }

  .founder {
    position: absolute;
    left: 34px;
    top: 200px;
  }
  .founder__name {
    font-family: 'Oswald', sans-serif;
    font-weight: 400;
    font-size: 31px;
    line-height: 1.05;
    letter-spacing: -0.3px;
  }
  .founder__role {
    font-family: 'Montserrat', sans-serif;
    font-weight: 300;
    font-size: 16px;
    line-height: 1.2;
  }

  .contact {
    position: absolute;
    left: 34px;
    top: 268px;
    list-style: none;
    font-family: 'Montserrat', sans-serif;
    font-weight: 300;
    font-size: 16px;
    letter-spacing: 0.2px;
  }
  .contact__item {
    display: flex;
    align-items: center;
    height: 22px;
  }
  .contact__icon {
    width: 16px;
    height: 16px;
    margin-right: 6px;
    flex: none;
  }

  .brand-disc {
    position: absolute;
    left: 246px;
    top: 26px;
    width: 316px;
    height: 316px;
  }
</style>
</head>
<body>
<main class="canvas">

  <section class="card card--front" aria-label="Card front">
    <div class="wordmark">arabesque studio</div>

    <div class="founder">
      <h1 class="founder__name">Claire Dufour</h1>
      <p class="founder__role">Founder &amp; Director</p>
    </div>

    <ul class="contact">
      <li class="contact__item">
        <svg class="contact__icon" viewBox="0 0 16 16" aria-hidden="true">
          <path d="M3.2 1.5l2.4 2.6-1.3 1.6c.8 1.9 2.2 3.4 4.1 4.3l1.6-1.3 2.6 2.3-1.5 2.4C6.5 13.2 2.7 9.4 1 4.7z" fill="#fff"/>
          <path d="M9.5 2.2a4.5 4.5 0 0 1 4.2 4.2M9.3 4.4a2.4 2.4 0 0 1 2.2 2.2" stroke="#fff" stroke-width="1.2" fill="none"/>
        </svg>
        022-555 010 247
      </li>
      <li class="contact__item">
        <svg class="contact__icon" viewBox="0 0 16 16" aria-hidden="true">
          <rect x="0.5" y="3" width="15" height="10" fill="#fff"/>
          <path d="M0.5 3l7.5 6 7.5-6M0.5 13l5.5-5M15.5 13l-5.5-5" stroke="#f3e888" stroke-width="1" fill="none"/>
        </svg>
        hello@arabesque.ch
      </li>
      <li class="contact__item">
        <svg class="contact__icon" viewBox="0 0 16 16" aria-hidden="true">
          <g stroke="#fff" stroke-width="1.1" fill="none">
            <circle cx="8" cy="8" r="7"/>
            <ellipse cx="8" cy="8" rx="3" ry="7"/>
            <path d="M1 8h14M2 4.5h12M2 11.5h12"/>
          </g>
        </svg>
        www.arabesque-studio.ch
      </li>
    </ul>

    <svg class="brand-disc" viewBox="0 0 316 316" aria-hidden="true">
      <circle cx="158" cy="158" r="158" fill="#ffffff"/>
    </svg>
  </section>

  <section class="card card--back" aria-label="Card back">
    <div class="wordmark">arabesque studio</div>
  </section>

</main>
</body>
</html>
```